Veterinary Power Point Template/Master

Dear Creatives,
we would need a Power Point Template that can be used for internal and external presentations. It'll mostly be needed to create B2B presentations at congresses or seminars, at which our vets attend as podium guests and lecturers.

What is important?
We see ourselves as highly professional, clean and innovative. One of our greatest mission is to build our work on latest medical research and the latest technology within veterinary medicine.
Therefore, our design should represent exactly this and look modern, professional and clinical.

Which slides do we need? What should they include?
- title
- section slides
- agenda
- Team slides to introduce our personell
- classic title & content
- slides to include different media and text options
- page numbers
- date
- our logo
- icons (if possible)

Unfortunately, we do not have an english version of our website yet, but feel free to browse through it to get a feeling for our appearance and values: https://www.tierpraxamo.at

We will also attach our little brand booklet as a guidance for you. BUT feel free to think out of the box and create a beautiful PPT design which is fun to watch.

Thrilled to see your great work already!

Target Market(s)

Austria

Industry/Entity Type

veterinary medicine

Font styles to use
Sans Serif
Other font styles liked:
• please only use Roboto font

Requirements
Must have
• items described in the creative brief
Nice to have
• animations and fancy transitions
Should not have
• Comic Sans or classic PPT Preset Designs

```html
<!DOCTYPE html>
<html lang="en">
<head>
<meta charset="utf-8">
<title>Tierpraxamo – Presentation Template</title>
<link href="https://fonts.googleapis.com/css2?family=Roboto:wght@300;400;500;700&display=swap" rel="stylesheet">
<style>
:root{
  --navy:#263646;
  --navy-soft:#3a4a5a;
  --gold:#d49f00;
  --green:#1e9e6a;
  --rust:#b8501b;
  --light:#f3f3f3;
  --white:#ffffff;
  --text:#4a4f55;
}
*{box-sizing:border-box;margin:0;padding:0}
html,body{width:1200px;height:2606px;overflow:hidden}
body{background:linear-gradient(#000 0,#050505 800px,#141414 2606px);font-family:'Roboto',sans-serif;color:var(--navy);position:relative}

/* ---------- hero title slide ---------- */
.hero{position:absolute;left:160px;top:85px;width:870px;height:487px;background:var(--light);overflow:hidden}
.hero-photo{position:absolute;left:433px;top:0;width:437px;height:487px;background:linear-gradient(135deg,#b9c8d6 0%,#e9d2c3 40%,#9fb6cf 70%,#e7c3a8 100%)}
.hero-band{position:absolute;left:0;top:122px;width:720px;height:243px;background:var(--white);border-bottom:2px solid #d7d7d7}
.hero-disc{position:absolute;left:520px;top:118px;width:264px;height:264px;border-radius:50%;background:var(--white);box-shadow:0 0 0 3px #e5e5e5}
.hero-disc::after{content:"";position:absolute;left:28px;top:28px;width:208px;height:208px;border-radius:50%;background:var(--navy)}
.hero-brand{position:absolute;left:48px;top:46px;display:flex;align-items:center;gap:12px}
.hero-dot{width:22px;height:22px;border-radius:50%;background:var(--navy)}
.hero-name{font-size:28px;font-weight:500;color:var(--navy);line-height:1}
.hero-title{position:absolute;left:70px;top:160px;font-size:43px;font-weight:700;line-height:1.03;color:var(--navy)}
.hero-sub{position:absolute;left:70px;top:252px;font-size:19px;font-weight:300;color:var(--navy)}
.hero-date{position:absolute;left:72px;top:310px;font-size:10px;font-weight:400;letter-spacing:3px;color:var(--navy)}
.hero-copy{position:absolute;left:50px;top:420px;font-size:8.5px;font-weight:400;letter-spacing:2.5px;color:var(--navy)}

/* ---------- slide grid ---------- */
.slide{position:absolute;width:362px;height:205px;background:var(--white);overflow:hidden}
.c1{left:39px}.c2{left:412px}.c3{left:786px}
.r1{top:826px}.r2{top:1042px}.r3{top:1257px}.r4{top:1472px}
.r5{top:1688px}.r6{top:1903px}.r7{top:2118px}.r8{top:2334px}
.abs{position:absolute}
.ph{position:absolute;background:linear-gradient(135deg,#c3d2df,#eef1f4 45%,#a9bfd4)}
.ph.warm{background:linear-gradient(135deg,#9fb4c9,#e4cbb8 50%,#c7d6e3)}
.ph.blue{background:linear-gradient(135deg,#1f4f86,#6ea2d4 55%,#d5e6f3)}
.ph.face{background:linear-gradient(160deg,#d7d9dc,#a9aeb4)}

.brand{display:flex;align-items:center;gap:5px}
.brand .dot{width:9px;height:9px;border-radius:50%;background:var(--navy)}
.brand .name{font-size:10px;font-weight:500;line-height:1;color:var(--navy)}
.on-dark .dot{background:var(--white)}
.on-dark .name{color:var(--white)}
.title{font-size:15.5px;font-weight:700;line-height:1.06;color:var(--navy)}
.title .lt{font-weight:400}
.subt{font-size:6.5px;margin-top:4px}
.date{font-size:3.6px;letter-spacing:1px;font-weight:700}
.fine{font-size:3.4px;letter-spacing:.6px;font-weight:700}

.h{font-size:14px;font-weight:500;color:var(--navy);letter-spacing:.2px}
.h b{font-weight:700}
.bars{display:flex;gap:2px;margin-top:3px}
.bars i{display:block;width:9px;height:4px}
.bars i:nth-child(1){background:var(--green)}
.bars i:nth-child(2){background:var(--gold)}
.bars i:nth-child(3){background:var(--rust)}
.txt{font-size:3.6px;line-height:1.4;color:var(--text)}
.small-h{font-size:5.5px;font-weight:500;color:var(--navy)}

.foot{position:absolute;left:9px;right:9px;bottom:6px;height:13px;display:flex;align-items:center;justify-content:space-between}
.foot .brand .dot{width:6px;height:6px}
.foot .brand .name{font-size:5.5px}
.foot .rights{display:flex;align-items:center;gap:3px;font-size:3.2px;font-weight:700}
.foot .pg{width:8px;height:8px;border-radius:50%;background:var(--navy);border:1px solid var(--gold)}

.ring{position:absolute;border-radius:50%}
.icon-c{position:absolute;border-radius:50%;display:flex;align-items:center;justify-content:center}
.icon-s{position:absolute;display:flex;align-items:center;justify-content:center}

.pill{position:absolute;height:40px;border:1px solid #e1e1e1;border-radius:20px;background:var(--white)}
.avatar{position:absolute;width:44px;height:44px;border-radius:50%;border:2px solid var(--gold);background:linear-gradient(160deg,#d7d9dc,#a9aeb4)}

table.data{border-collapse:collapse;font-size:4.3px;color:var(--navy)}
table.data td,table.data th{height:11.2px;padding:0 3px;border-bottom:1px solid #e6e6e6;text-align:center}
table.data th{color:var(--white);font-weight:700;font-size:4.2px}
table.data td:first-child,table.data th:first-child{text-align:left;font-weight:700;width:102px}
</style>
</head>
<body>

<!-- Hero: title slide -->
<section class="hero" aria-label="Title slide">
  <div class="hero-photo" role="img" aria-label="Laboratory photo: gloved hands with test tubes"></div>
  <div class="hero-band"></div>
  <div class="hero-disc"></div>
  <div class="hero-brand"><span class="hero-dot"></span><span class="hero-name">Tierpraxamo</span></div>
  <h1 class="hero-title">PRESENTATION<br>TITLE GOES HERE</h1>
  <p class="hero-sub">Subtitle of Presentation Goes Here</p>
  <p class="hero-date">Wednesday, September 13, 2023</p>
  <p class="hero-copy">© Tierpraxamo 2023. All Rights Reserved.</p>
</section>

<!-- Row 1 -->
<section class="slide c1 r1" style="background:var(--light)">
  <div class="ph warm" style="left:182px;top:0;width:180px;height:205px" role="img" aria-label="Laboratory photo with test tubes"></div>
  <div class="abs" style="left:0;top:54px;width:320px;height:100px;background:#fff;border-bottom:1px solid #ddd"></div>
  <div class="abs" style="left:222px;top:50px;width:106px;height:106px;border-radius:50%;background:#fff;box-shadow:0 0 0 2px #e5e5e5"></div>
  <div class="abs" style="left:234px;top:62px;width:82px;height:82px;border-radius:50%;background:var(--navy)"></div>
  <div class="brand abs" style="left:18px;top:20px"><span class="dot"></span><span class="name">Tierpraxamo</span></div>
  <div class="abs" style="left:29px;top:70px"><div class="title">PRESENTATION<br>TITLE GOES HERE</div><div class="subt">Subtitle of Presentation Goes Here</div></div>
  <div class="abs date" style="left:29px;top:130px">Wednesday, September 13, 2023</div>
  <div class="abs fine" style="left:20px;top:178px">© Tierpraxamo 2023. All Rights Reserved.</div>
</section>

<section class="slide c2 r1" style="background:var(--navy);color:#fff">
  <div class="abs" style="left:185px;top:30px;width:170px;height:170px;border-radius:50%;background:var(--navy-soft)"></div>
  <div class="abs" style="left:290px;top:105px;width:70px;height:70px;border-radius:50%;background:#5c5630"></div>
  <div class="brand abs on-dark" style="left:30px;top:40px"><span class="dot"></span><span class="name">Tierpraxamo</span></div>
  <div class="abs" style="left:29px;top:84px"><div class="title" style="color:#fff">PRESENTATION<br>TITLE GOES HERE</div><div class="subt">Subtitle of Presentation Goes Here</div></div>
  <div class="abs date" style="left:29px;top:144px">Wednesday, September 15, 2023</div>
  <div class="abs fine" style="left:29px;top:170px">© Tierpraxamo 2023. All Rights Reserved.</div>
</section>

<section class="slide c3 r1" style="background:linear-gradient(100deg,#f6f6f6 40%,#c6c6c6)">
  <div class="abs" style="left:185px;top:30px;width:170px;height:170px;border-radius:50%;background:#dcdcdc"></div>
  <div class="abs" style="left:290px;top:105px;width:70px;height:70px;border-radius:50%;background:#d2bd7b"></div>
  <div class="brand abs" style="left:30px;top:40px"><span class="dot"></span><span class="name">Tierpraxamo</span></div>
  <div class="abs" style="left:29px;top:84px"><div class="title">PRESENTATION<br>TITLE GOES HERE</div><div class="subt">Subtitle of Presentation Goes Here</div></div>
  <div class="abs date" style="left:29px;top:144px">Wednesday, September 15, 2023</div>
  <div class="abs fine" style="left:29px;top:170px">© Tierpraxamo 2023. All Rights Reserved.</div>
</section>

<!-- Row 2 -->
<section class="slide c1 r2" style="background:#fff">
  <div class="abs" style="left:0;top:52px;width:300px;height:100px;background:var(--navy)"></div>
  <div class="ring" style="left:206px;top:32px;width:138px;height:138px;background:var(--gold)"></div>
  <div class="ring" style="left:218px;top:48px;width:104px;height:104px;background:var(--navy)"></div>
  <div class="ring" style="left:224px;top:54px;width:92px;height:92px;background:#fff"></div>
  <div class="brand abs" style="left:18px;top:20px"><span class="dot"></span><span class="name">Tierpraxamo</span></div>
  <div class="abs" style="left:29px;top:66px;color:#fff"><div class="title" style="color:#fff">PRESENTATION<br><span class="lt">TITLE GOES HERE</span></div><div class="subt">Subtitle of Presentation Goes Here</div></div>
  <div class="abs date" style="left:29px;top:128px;color:#fff">Wednesday, September 15, 2023</div>
  <div class="abs fine" style="left:20px;top:178px">© Tierpraxamo 2023. All Rights Reserved.</div>
</section>

<section class="slide c2 r2" style="background:var(--navy)">
  <div class="abs" style="left:0;top:52px;width:300px;height:100px;background:#fff"></div>
  <div class="ring" style="left:206px;top:32px;width:138px;height:138px;background:var(--gold)"></div>
  <div class="ring" style="left:218px;top:48px;width:104px;height:104px;background:#fff"></div>
  <div class="ring" style="left:224px;top:54px;width:92px;height:92px;background:var(--navy)"></div>
  <div class="brand abs on-dark" style="left:18px;top:20px"><span class="dot"></span><span class="name">Tierpraxamo</span></div>
  <div class="abs" style="left:29px;top:66px"><div class="title">PRESENTATION<br><span class="lt">TITLE GOES HERE</span></div><div class="subt">Subtitle of Presentation Goes Here</div></div>
  <div class="abs date" style="left:29px;top:128px">Wednesday, September 15, 2023</div>
  <div class="abs fine" style="left:20px;top:178px;color:#fff">© Tierpraxamo 2023. All Rights Reserved.</div>
</section>

<section class="slide c3 r2" style="background:var(--light)">
  <div class="abs" style="left:0;top:52px;width:300px;height:100px;background:#fff"></div>
  <div class="ring" style="left:206px;top:32px;width:138px;height:138px;background:var(--gold)"></div>
  <div class="ring" style="left:218px;top:48px;width:104px;height:104px;background:#fff"></div>
  <div class="ring" style="left:224px;top:54px;width:92px;height:92px;background:var(--navy)"></div>
  <div class="brand abs" style="left:18px;top:20px"><span class="dot"></span><span class="name">Tierpraxamo</span></div>
  <div class="abs" style="left:29px;top:66px"><div class="title">PRESENTATION<br><span class="lt">TITLE GOES HERE</span></div><div class="subt">Subtitle of Presentation Goes Here</div></div>
  <div class="abs date" style="left:29px;top:128px">Wednesday, September 15, 2023</div>
  <div class="abs fine" style="left:20px;top:178px">© Tierpraxamo 2023. All Rights Reserved.</div>
</section>

<!-- Row 3 -->
<section class="slide c1 r3" style="background:#fff">
  <div class="ph" style="left:246px;top:0;width:116px;height:205px" role="img" aria-label="Photo of laboratory test tubes"></div>
  <div class="abs" style="left:0;top:15px;width:255px;height:160px;background:var(--light)"></div>
  <div class="abs" style="left:18px;top:90px"><div class="h"><b>AGENDA</b></div><div class="bars"><i></i><i></i><i></i></div></div>
  <ol class="abs" style="left:122px;top:40px;list-style:none;font-size:6.5px;color:var(--navy)">
    <li style="height:21px"><span style="color:#aaa">1.</span> <span style="border-left:2px solid var(--green);padding-left:3px">Dolor Sit Amet</span></li>
    <li style="height:21px"><span style="color:#aaa">3.</span> <span style="border-left:2px solid var(--gold);padding-left:3px">Consectetur Adipiscing</span></li>
    <li style="height:21px"><span style="color:#aaa">5.</span> <span style="border-left:2px solid var(--rust);padding-left:3px">Vivamus Eu Dui Ex</span></li>
    <li style="height:21px"><span style="color:#aaa">2.</span> <span style="border-left:2px solid var(--green);padding-left:3px">Dapibus Dignissim</span></li>
    <li style="height:21px"><span style="color:#aaa">4.</span> <span style="border-left:2px solid var(--gold);padding-left:3px">Vivamus Eu Dui Ex</span></li>
    <li style="height:21px"><span style="color:#aaa">6.</span> <span style="border-left:2px solid var(--rust);padding-left:3px">Consectetur Adipiscing</span></li>
  </ol>
  <div class="foot"><div class="brand"><span class="dot"></span><span class="name">Tierpraxamo</span></div><div class="rights">© Tierpraxamo 2023. All Rights Reserved.<span class="pg"></span></div></div>
</section>

<section class="slide c2 r3">
  <div class="ph blue" style="left:180px;top:0;width:150px;height:162px" role="img" aria-label="Photo of a researcher in a lab with digital overlay"></div>
  <div class="abs" style="left:34px;top:32px"><div class="h"><b>ABOUT</b> US</div><div class="bars"><i></i><i></i><i></i></div></div>
  <p class="abs txt" style="left:34px;top:68px;width:132px">We are a specialist small animal clinic in Austria. Our work is built on current veterinary research and modern diagnostic technology. Our vets teach at congresses and seminars and share their knowledge with colleagues. Each patient is examined with care, precision and respect. We invest in imaging, laboratory analysis and surgery so owners receive clear answers quickly. Our team meets regularly to review cases, discuss new studies and refine treatment plans for cats, dogs and other small animals.</p>
  <div class="foot"><div class="brand"><span class="dot"></span><span class="name">Tierpraxamo</span></div><div class="rights">© Tierpraxamo 2023. All Rights Reserved.<span class="pg"></span></div></div>
</section>

<section class="slide c3 r3">
  <div class="abs" style="left:18px;top:50px"><div class="h">OUR TEAM</div><div class="bars"><i></i><i></i><i></i></div></div>
  <p class="abs txt" style="left:18px;top:90px;width:112px">Our specialists combine clinical experience with ongoing research, bringing current methods into everyday practice.</p>
  <div class="ph face" style="left:142px;top:12px;width:66px;height:66px" role="img" aria-label="Portrait photo of team member"></div>
  <div class="ph face" style="left:212px;top:12px;width:66px;height:66px" role="img" aria-label="Portrait photo of team member"></div>
  <div class="ph face" style="left:282px;top:12px;width:66px;height:66px" role="img" aria-label="Portrait photo of team member"></div>
  <div class="abs" style="left:144px;top:84px;width:64px"><div class="small-h" style="font-size:4.5px;font-weight:700">Name Goes Here</div><div class="txt">Job Title Goes Here</div><p class="txt" style="margin-top:3px">Small animal surgery and orthopaedics.</p><div class="txt" style="font-weight:700;margin-top:3px;color:var(--navy)">Job Experience</div><p class="txt">• Ten years in clinic<br>• Lecturer at seminars</p></div>
  <div class="abs" style="left:214px;top:84px;width:64px"><div class="small-h" style="font-size:4.5px;font-weight:700">Name Goes Here</div><div class="txt">Job Title Goes Here</div><p class="txt" style="margin-top:3px">Internal medicine and diagnostics.</p><div class="txt" style="font-weight:700;margin-top:3px;color:var(--navy)">Job Experience</div><p class="txt">• Eight years in clinic<br>• Congress speaker</p></div>
  <div class="abs" style="left:284px;top:84px;width:64px"><div class="small-h" style="font-size:4.5px;font-weight:700">Name Goes Here</div><div class="txt">Job Title Goes Here</div><p class="txt" style="margin-top:3px">Imaging and cardiology care.</p><div class="txt" style="font-weight:700;margin-top:3px;color:var(--navy)">Job Experience</div><p class="txt">• Twelve years in clinic<br>• Research lead</p></div>
  <div class="foot"><div class="brand"><span class="dot"></span><span class="name">Tierpraxamo</span></div><div class="rights">© Tierpraxamo 2023. All Rights Reserved.<span class="pg"></span></div></div>
</section>

<!-- Row 4 -->
<section class="slide c1 r4">
  <div class="abs" style="left:18px;top:52px"><div class="h">OUR TEAM</div><div class="bars"><i></i><i></i><i></i></div></div>
  <p class="abs txt" style="left:18px;top:92px;width:112px">Meet the people who care for your patients every day.</p>
  <div class="pill" style="left:160px;top:20px;width:180px"></div>
  <div class="avatar" role="img" aria-label="Team member portrait" style="left:152px;top:18px"></div>
  <div class="abs" style="left:212px;top:25px;width:118px"><div class="small-h" style="font-size:4.5px;font-weight:700">Name Goes Here</div><div class="txt">Job Title Goes Here</div><p class="txt">Surgery and orthopaedics specialist.</p></div>
  <div class="pill" style="left:160px;top:78px;width:180px"></div>
  <div class="avatar" role="img" aria-label="Team member portrait" style="left:296px;top:76px"></div>
  <div class="abs" style="left:172px;top:83px;width:118px"><div class="small-h" style="font-size:4.5px;font-weight:700">Name Goes Here</div><div class="txt">Job Title Goes Here</div><p class="txt">Internal medicine specialist.</p></div>
  <div class="pill" style="left:160px;top:134px;width:180px"></div>
  <div class="avatar" role="img" aria-label="Team member portrait" style="left:152px;top:132px"></div>
  <div class="abs" style="left:212px;top:139px;width:118px"><div class="small-h" style="font-size:4.5px;font-weight:700">Name Goes Here</div><div class="txt">Job Title Goes Here</div><p class="txt">Imaging and cardiology specialist.</p></div>
  <div class="foot"><div class="brand"><span class="dot"></span><span class="name">Tierpraxamo</span></div><div class="rights">© Tierpraxamo 2023. All Rights Reserved.<span class="pg"></span></div></div>
</section>

<section class="slide c2 r4">
  <div class="abs" style="left:18px;top:16px"><div class="h">OUR TEAM</div><div class="bars"><i></i><i></i><i></i></div></div>
  <svg class="abs" style="left:0;top:0" width="362" height="205" aria-hidden="true">
    <line x1="108" y1="95" x2="155" y2="60" stroke="var(--green)" stroke-width="1"/>
    <line x1="108" y1="95" x2="155" y2="95" stroke="var(--gold)" stroke-width="1"/>
    <line x1="108" y1="95" x2="155" y2="150" stroke="var(--rust)" stroke-width="1"/>
  </svg>
  <div class="avatar" role="img" aria-label="Team lead portrait" style="left:42px;top:62px;width:64px;height:64px"></div>
  <div class="abs" style="left:24px;top:134px;width:100px;text-align:center"><div class="small-h" style="font-size:4.5px;font-weight:700">Name Goes Here</div><div class="txt">Job Title Goes Here</div><p class="txt">Medical director and head surgeon.</p></div>
  <div class="pill" style="left:162px;top:18px;width:180px"></div>
  <div class="avatar" role="img" aria-label="Team member portrait" style="left:152px;top:16px"></div>
  <div class="abs" style="left:212px;top:23px;width:118px"><div class="small-h" style="font-size:4.5px;font-weight:700">Name Goes Here</div><div class="txt">Job Title Goes Here</div><p class="txt">Surgery and orthopaedics.</p></div>
  <div class="pill" style="left:162px;top:74px;width:180px"></div>
  <div class="avatar" role="img" aria-label="Team member portrait" style="left:152px;top:72px"></div>
  <div class="abs" style="left:212px;top:79px;width:118px"><div class="small-h" style="font-size:4.5px;font-weight:700">Name Goes Here</div><div class="txt">Job Title Goes Here</div><p class="txt">Internal medicine.</p></div>
  <div class="pill" style="left:162px;top:130px;width:180px"></div>
  <div class="avatar" role="img" aria-label="Team member portrait" style="left:152px;top:128px"></div>
  <div class="abs" style="left:212px;top:135px;width:118px"><div class="small-h" style="font-size:4.5px;font-weight:700">Name Goes Here</div><div class="txt">Job Title Goes Here</div><p class="txt">Imaging and cardiology.</p></div>
  <div class="foot"><div class="brand"><span class="dot"></span><span class="name">Tierpraxamo</span></div><div class="rights">© Tierpraxamo 2023. All Rights Reserved.<span class="pg"></span></div></div>
</section>

<section class="slide c3 r4">
  <div class="abs" style="left:18px;top:16px"><div class="h"><b>HEADING</b> GOES HERE</div><div class="bars"><i></i><i></i><i></i></div></div>
  <div class="icon-c" style="left:58px;top:60px;width:40px;height:40px;background:var(--green)"><svg width="18" height="18" viewBox="0 0 18 18"><circle cx="9" cy="6" r="4" fill="#fff"/><path d="M2 17c0-5 14-5 14 0z" fill="#fff"/></svg></div>
  <div class="icon-c" style="left:160px;top:60px;width:40px;height:40px;background:var(--gold)"><svg width="18" height="18" viewBox="0 0 18 18"><circle cx="9" cy="7" r="5" fill="none" stroke="#fff" stroke-width="2"/><rect x="6" y="12" width="6" height="4" fill="#fff"/></svg></div>
  <div class="icon-c" style="left:260px;top:60px;width:40px;height:40px;background:var(--rust)"><svg width="18" height="18" viewBox="0 0 18 18"><circle cx="9" cy="8" r="6" fill="#fff"/><circle cx="9" cy="8" r="3" fill="var(--rust)"/></svg></div>
  <div class="abs" style="left:28px;top:110px;width:100px;text-align:center"><div class="small-h" style="font-size:7px"><b>Title</b> Goes Here</div><p class="txt" style="margin-top:4px">Modern diagnostics help us detect disease early and treat it precisely.</p></div>
  <div class="abs" style="left:130px;top:110px;width:100px;text-align:center"><div class="small-h" style="font-size:7px"><b>Title</b> Goes Here</div><p class="txt" style="margin-top:4px">New ideas from research shape how we plan each treatment.</p></div>
  <div class="abs" style="left:230px;top:110px;width:100px;text-align:center"><div class="small-h" style="font-size:7px"><b>Title</b> Goes Here</div><p class="txt" style="margin-top:4px">Quality standards guide every step of our clinical work.</p></div>
  <div class="foot"><div class="brand"><span class="dot"></span><span class="name">Tierpraxamo</span></div><div class="rights">© Tierpraxamo 2023. All Rights Reserved.<span class="pg"></span></div></div>
</section>

<!-- Row 5 -->
<section class="slide c1 r5">
  <div class="ph" style="left:10px;top:10px;width:112px;height:104px" role="img" aria-label="Photo of a scientist in a lab"></div>
  <div class="ph warm" style="left:126px;top:10px;width:112px;height:104px" role="img" aria-label="Photo of hands using a tablet"></div>
  <div class="ph blue" style="left:242px;top:10px;width:112px;height:104px" role="img" aria-label="Photo of test tubes"></div>
  <div class="abs" style="left:10px;top:120px;width:112px;text-align:center"><div class="small-h">Heading Goes Here</div></div>
  <div class="abs" style="left:126px;top:120px;width:112px;text-align:center"><div class="small-h">Heading Goes Here</div></div>
  <div class="abs" style="left:242px;top:120px;width:112px;text-align:center"><div class="small-h">Heading Goes Here</div></div>
  <p class="abs txt" style="left:16px;top:132px;width:100px">• Precise lab work.<br>• Results within hours.<br>• Clear reports for owners.</p>
  <p class="abs txt" style="left:132px;top:132px;width:100px">• Digital patient records.<br>• Shared case notes.<br>• Secure data storage.</p>
  <p class="abs txt" style="left:248px;top:132px;width:100px">• Current research.<br>• Tested protocols.<br>• Ongoing training.</p>
  <div class="foot"><div class="brand"><span class="dot"></span><span class="name">Tierpraxamo</span></div><div class="rights">© Tierpraxamo 2023. All Rights Reserved.<span class="pg"></span></div></div>
</section>

<section class="slide c2 r5">
  <div class="abs" style="left:18px;top:16px"><div class="h"><b>HEADING</b> GOES HERE</div><div class="bars"><i></i><i></i><i></i></div></div>
  <div class="abs" style="left:0;top:58px;width:362px;height:58px;background:var(--light)"></div>
  <p class="abs txt" style="left:18px;top:66px;width:150px">Our vets attend congresses as speakers and bring the latest findings back into daily clinical routine for every patient.</p>
  <p class="abs txt" style="left:192px;top:66px;width:150px">We review new studies together and update our protocols when the evidence shows a better way to care.</p>
  <div class="icon-c" style="left:16px;top:130px;width:24px;height:24px;background:var(--green)"><svg width="10" height="10"><circle cx="5" cy="4" r="3.5" fill="#fff"/></svg></div>
  <div class="icon-s" style="left:128px;top:130px;width:24px;height:24px;background:var(--gold);border-radius:4px"><svg width="10" height="10"><rect x="1" y="5" width="2" height="4" fill="#fff"/><rect x="4" y="3" width="2" height="6" fill="#fff"/><rect x="7" y="1" width="2" height="8" fill="#fff"/></svg></div>
  <div class="icon-s" style="left:240px;top:130px;width:24px;height:24px;background:var(--rust);border-radius:4px"><svg width="10" height="10"><path d="M1 4h2v5H1zM4 4l3-3v3h2v5H4z" fill="#fff"/></svg></div>
  <div class="abs" style="left:44px;top:128px;width:76px"><div class="small-h" style="color:var(--green);font-size:4.8px">Heading Goes Here</div><p class="txt">Short note about this point and its benefit.</p></div>
  <div class="abs" style="left:156px;top:128px;width:76px"><div class="small-h" style="color:var(--gold);font-size:4.8px">Heading Goes Here</div><p class="txt">Short note about this point and its benefit.</p></div>
  <div class="abs" style="left:268px;top:128px;width:76px"><div class="small-h" style="color:var(--rust);font-size:4.8px">Heading Goes Here</div><p class="txt">Short note about this point and its benefit.</p></div>
  <div class="foot"><div class="brand"><span class="dot"></span><span class="name">Tierpraxamo</span></div><div class="rights">© Tierpraxamo 2023. All Rights Reserved.<span class="pg"></span></div></div>
</section>

<section class="slide c3 r5" style="background:var(--navy)">
  <div class="abs" style="left:185px;top:30px;width:170px;height:170px;border-radius:50%;background:var(--navy-soft)"></div>
  <div class="abs" style="left:290px;top:105px;width:70px;height:70px;border-radius:50%;background:#5c5630"></div>
  <div class="brand abs on-dark" style="left:32px;top:80px"><span class="dot" style="width:6px;height:6px"></span><span class="name" style="font-size:6px">Tierpraxamo</span></div>
  <div class="abs" style="left:32px;top:100px;font-size:14px;font-weight:500;color:#fff">Section Break</div>
  <p class="abs txt" style="left:32px;top:122px;width:120px;color:#dfe4e9">A short line that introduces the next part of this talk and its topic.</p>
</section>

<!-- Row 6 -->
<section class="slide c1 r6">
  <div class="abs" style="left:18px;top:16px"><div class="h"><b>HEADING</b> Goes Here</div><div class="bars"><i></i><i></i><i></i></div></div>
  <div class="icon-s" style="left:24px;top:56px;width:26px;height:26px;background:var(--green)"><svg width="12" height="12"><path d="M4 1h4v4l3 6H1l3-6z" fill="#fff"/></svg></div>
  <div class="icon-s" style="left:186px;top:56px;width:26px;height:26px;background:var(--gold)"><svg width="12" height="12"><path d="M1 5h10a5 5 0 0 1-10 0z" fill="#fff"/></svg></div>
  <div class="icon-s" style="left:24px;top:122px;width:26px;height:26px;background:var(--rust)"><svg width="12" height="12"><circle cx="6" cy="6" r="5" fill="none" stroke="#fff" stroke-width="1.5"/><path d="M6 3v3h2" stroke="#fff" fill="none"/></svg></div>
  <div class="icon-s" style="left:186px;top:122px;width:26px;height:26px;background:var(--navy)"><svg width="12" height="12"><rect x="1" y="7" width="2" height="4" fill="#fff"/><rect x="5" y="4" width="2" height="7" fill="#fff"/><rect x="9" y="1" width="2" height="10" fill="#fff"/></svg></div>
  <div class="abs" style="left:56px;top:56px;width:110px"><div class="small-h" style="color:var(--green);font-size:5px;font-weight:700">Heading Goes Here</div><p class="txt">Our laboratory runs blood and tissue analysis on site, so results reach the treating vet within hours.</p></div>
  <div class="abs" style="left:218px;top:56px;width:110px"><div class="small-h" style="color:var(--gold);font-size:5px;font-weight:700">Heading Goes Here</div><p class="txt">Pain management and gentle anaesthesia protocols keep every patient calm and safe during care.</p></div>
  <div class="abs" style="left:56px;top:122px;width:110px"><div class="small-h" style="color:var(--rust);font-size:5px;font-weight:700">Heading Goes Here</div><p class="txt">Emergency service is available around the clock with a specialist on call for urgent cases.</p></div>
  <div class="abs" style="left:218px;top:122px;width:110px"><div class="small-h" style="font-size:5px;font-weight:700">Heading Goes Here</div><p class="txt">We measure outcomes and share the data openly with partners at conferences.</p></div>
  <div class="foot"><div class="brand"><span class="dot"></span><span class="name">Tierpraxamo</span></div><div class="rights">© Tierpraxamo 2023. All Rights Reserved.<span class="pg"></span></div></div>
</section>

<section class="slide c2 r6">
  <div class="abs" style="left:18px;top:16px"><div class="h"><b>HEADING</b> GOES HERE</div><div class="bars"><i></i><i></i><i></i></div></div>
  <svg class="abs" style="left:0;top:62px" width="362" height="30" aria-hidden="true">
    <line x1="0" y1="14" x2="320" y2="14" stroke="#bbb" stroke-dasharray="2 2"/>
    <path d="M318 11l5 3-5 3" fill="none" stroke="#bbb"/>
    <circle cx="72" cy="14" r="11" fill="#fff" stroke="#ddd"/><circle cx="145" cy="14" r="11" fill="#fff" stroke="#ddd"/>
    <circle cx="217" cy="14" r="11" fill="#fff" stroke="#ddd"/><circle cx="290" cy="14" r="11" fill="#fff" stroke="#ddd"/>
    <text x="72" y="18" font-size="10" font-family="Roboto,sans-serif" text-anchor="middle" fill="var(--navy)">1</text>
    <text x="145" y="18" font-size="10" font-family="Roboto,sans-serif" text-anchor="middle" fill="var(--green)">2</text>
    <text x="217" y="18" font-size="10" font-family="Roboto,sans-serif" text-anchor="middle" fill="var(--gold)">3</text>
    <text x="290" y="18" font-size="10" font-family="Roboto,sans-serif" text-anchor="middle" fill="var(--rust)">4</text>
  </svg>
  <div class="abs" style="left:42px;top:100px;width:60px;text-align:center"><div class="small-h" style="font-size:5px;font-weight:700">Heading<br>Goes Here</div><p class="txt" style="margin-top:3px">First contact and full health check.</p></div>
  <div class="abs" style="left:115px;top:100px;width:60px;text-align:center"><div class="small-h" style="font-size:5px;font-weight:700;color:var(--green)">Heading<br>Goes Here</div><p class="txt" style="margin-top:3px">Lab tests and imaging on site.</p></div>
  <div class="abs" style="left:187px;top:100px;width:60px;text-align:center"><div class="small-h" style="font-size:5px;font-weight:700;color:var(--gold)">Heading<br>Goes Here</div><p class="txt" style="margin-top:3px">Treatment plan shared with owners.</p></div>
  <div class="abs" style="left:260px;top:100px;width:60px;text-align:center"><div class="small-h" style="font-size:5px;font-weight:700;color:var(--rust)">Heading<br>Goes Here</div><p class="txt" style="margin-top:3px">Follow-up visits and aftercare.</p></div>
  <div class="foot"><div class="brand"><span class="dot"></span><span class="name">Tierpraxamo</span></div><div class="rights">© Tierpraxamo 2023. All Rights Reserved.<span class="pg"></span></div></div>
</section>

<section class="slide c3 r6">
  <div class="abs" style="left:18px;top:16px"><div class="h"><b>HEADING</b> GOES HERE</div><div class="bars"><i></i><i></i><i></i></div></div>
  <svg class="abs" style="left:126px;top:50px" width="110" height="110" viewBox="0 0 110 110" aria-hidden="true">
    <circle cx="55" cy="55" r="44" fill="none" stroke="var(--navy)" stroke-width="18" stroke-dasharray="67 209.5" transform="rotate(-90 55 55)"/>
    <circle cx="55" cy="55" r="44" fill="none" stroke="var(--green)" stroke-width="18" stroke-dasharray="67 209.5" stroke-dashoffset="-69" transform="rotate(-90 55 55)"/>
    <circle cx="55" cy="55" r="44" fill="none" stroke="var(--gold)" stroke-width="18" stroke-dasharray="67 209.5" stroke-dashoffset="-138" transform="rotate(-90 55 55)"/>
    <circle cx="55" cy="55" r="44" fill="none" stroke="var(--rust)" stroke-width="18" stroke-dasharray="67 209.5" stroke-dashoffset="-207" transform="rotate(-90 55 55)"/>
    <circle cx="55" cy="55" r="27" fill="#fff"/><circle cx="55" cy="55" r="22" fill="var(--navy)"/>
  </svg>
  <div class="abs" style="left:18px;top:62px;width:104px;text-align:center"><div class="small-h" style="font-size:5px;font-weight:700">Heading Goes Here</div><p class="txt">Short note about this service area and why it matters.</p></div>
  <div class="abs" style="left:18px;top:130px;width:104px;text-align:center"><div class="small-h" style="font-size:5px;font-weight:700;color:var(--rust)">Heading Goes Here</div><p class="txt">Short note about this service area and why it matters.</p></div>
  <div class="abs" style="left:242px;top:62px;width:104px"><div class="small-h" style="font-size:5px;font-weight:700;color:var(--green)">Heading Goes Here</div><p class="txt">Short note about this service area and why it matters.</p></div>
  <div class="abs" style="left:242px;top:130px;width:104px"><div class="small-h" style="font-size:5px;font-weight:700;color:var(--gold)">Heading Goes Here</div><p class="txt">Short note about this service area and why it matters.</p></div>
  <div class="foot"><div class="brand"><span class="dot"></span><span class="name">Tierpraxamo</span></div><div class="rights">© Tierpraxamo 2023. All Rights Reserved.<span class="pg"></span></div></div>
</section>

<!-- Row 7 -->
<section class="slide c1 r7" style="background:linear-gradient(100deg,#f6f6f6 40%,#c6c6c6)">
  <div class="abs" style="left:185px;top:30px;width:170px;height:170px;border-radius:50%;background:#dcdcdc"></div>
  <div class="abs" style="left:290px;top:105px;width:70px;height:70px;border-radius:50%;background:#d2bd7b"></div>
  <div class="brand abs" style="left:32px;top:80px"><span class="dot" style="width:6px;height:6px"></span><span class="name" style="font-size:6px">Tierpraxamo</span></div>
  <div class="abs" style="left:32px;top:100px;font-size:14px;font-weight:500;color:var(--navy)">Section Break</div>
  <p class="abs txt" style="left:32px;top:122px;width:120px">A short line that introduces the next part of this talk and its topic.</p>
</section>

<section class="slide c2 r7">
  <div class="ph blue" style="left:20px;top:0;width:156px;height:170px" role="img" aria-label="Photo of a researcher with a digital hexagon overlay"></div>
  <div class="abs" style="left:198px;top:22px"><div class="h" style="font-size:13px"><b>HEADING</b></div><p class="txt" style="width:140px;font-size:4px">A brief sentence that sets the context for the figures below.</p><div class="bars"><i></i><i></i><i></i></div></div>
  <svg class="abs" style="left:198px;top:76px" width="150" height="60" aria-hidden="true">
    <circle cx="32" cy="28" r="23" fill="none" stroke="#e6e6e6" stroke-width="3"/>
    <circle cx="32" cy="28" r="23" fill="none" stroke="var(--navy)" stroke-width="3" stroke-dasharray="118.5 144.5" transform="rotate(-90 32 28)"/>
    <text x="32" y="32" text-anchor="middle" font-size="11" font-family="Roboto,sans-serif" fill="var(--navy)">82%</text>
    <circle cx="108" cy="28" r="23" fill="none" stroke="#eee" stroke-width="3"/>
    <circle cx="108" cy="28" r="23" fill="none" stroke="var(--gold)" stroke-width="3" stroke-dasharray="136 144.5" transform="rotate(-90 108 28)"/>
    <text x="108" y="32" text-anchor="middle" font-size="11" font-family="Roboto,sans-serif" fill="var(--gold)">94%</text>
  </svg>
  <p class="abs txt" style="left:200px;top:140px;width:60px;text-align:center">Share of cases with a confirmed diagnosis on the first visit.</p>
  <p class="abs txt" style="left:276px;top:140px;width:60px;text-align:center">Share of owners who rate our care as very good.</p>
  <div class="foot"><div class="brand"><span class="dot"></span><span class="name">Tierpraxamo</span></div><div class="rights">© Tierpraxamo 2023. All Rights Reserved.<span class="pg"></span></div></div>
</section>

<section class="slide c3 r7">
  <div class="abs" style="left:18px;top:16px"><div class="h"><b>CHART</b> SLIDE</div><div class="bars"><i></i><i></i><i></i></div></div>
  <svg class="abs" style="left:0;top:52px" width="362" height="90" aria-hidden="true">
    <circle cx="80" cy="42" r="34" fill="none" stroke="var(--green)" stroke-width="4" stroke-dasharray="137 213.6" transform="rotate(-90 80 42)"/>
    <text x="80" y="47" text-anchor="middle" font-size="14" font-family="Roboto,sans-serif" fill="var(--green)">64%</text>
    <circle cx="181" cy="42" r="34" fill="none" stroke="var(--gold)" stroke-width="4" stroke-dasharray="175 213.6" transform="rotate(-90 181 42)"/>
    <text x="181" y="47" text-anchor="middle" font-size="14" font-family="Roboto,sans-serif" fill="var(--gold)">82%</text>
    <circle cx="282" cy="42" r="34" fill="none" stroke="var(--rust)" stroke-width="4" stroke-dasharray="201 213.6" transform="rotate(-90 282 42)"/>
    <text x="282" y="47" text-anchor="middle" font-size="14" font-family="Roboto,sans-serif" fill="var(--rust)">94%</text>
  </svg>
  <div class="abs" style="left:40px;top:142px;width:80px;text-align:center"><div class="small-h">Title Goes Here</div><p class="txt">Short note that explains this value.</p></div>
  <div class="abs" style="left:141px;top:142px;width:80px;text-align:center"><div class="small-h">Title Goes Here</div><p class="txt">Short note that explains this value.</p></div>
  <div class="abs" style="left:242px;top:142px;width:80px;text-align:center"><div class="small-h">Title Goes Here</div><p class="txt">Short note that explains this value.</p></div>
  <div class="foot"><div class="brand"><span class="dot"></span><span class="name">Tierpraxamo</span></div><div class="rights">© Tierpraxamo 2023. All Rights Reserved.<span class="pg"></span></div></div>
</section>

<!-- Row 8 -->
<section class="slide c1 r8">
  <div class="abs" style="left:18px;top:16px"><div class="h"><b>HEADING</b> GOES HERE</div><div class="bars"><i></i><i></i><i></i></div></div>
  <svg class="abs" style="left:20px;top:50px" width="190" height="80" aria-hidden="true" font-family="Roboto,sans-serif" font-size="3.5" fill="#777">
    <line x1="12" y1="8" x2="186" y2="8" stroke="#eee"/><line x1="12" y1="24" x2="186" y2="24" stroke="#eee"/>
    <line x1="12" y1="40" x2="186" y2="40" stroke="#eee"/><line x1="12" y1="56" x2="186" y2="56" stroke="#eee"/>
    <line x1="12" y1="72" x2="186" y2="72" stroke="#ccc"/>
    <text x="4" y="10">6</text><text x="4" y="26">4</text><text x="4" y="42">3</text><text x="4" y="58">1</text><text x="4" y="74">0</text>
    <rect x="28" y="42" width="5" height="30" fill="var(--navy)"/><rect x="35" y="52" width="5" height="20" fill="var(--green)"/><rect x="42" y="56" width="5" height="16" fill="var(--gold)"/>
    <rect x="70" y="50" width="5" height="22" fill="var(--navy)"/><rect x="77" y="38" width="5" height="34" fill="var(--green)"/><rect x="84" y="56" width="5" height="16" fill="var(--gold)"/>
    <rect x="112" y="36" width="5" height="36" fill="var(--navy)"/><rect x="119" y="50" width="5" height="22" fill="var(--green)"/><rect x="126" y="44" width="5" height="28" fill="var(--gold)"/>
    <rect x="154" y="30" width="5" height="42" fill="var(--navy)"/><rect x="161" y="42" width="5" height="30" fill="var(--green)"/><rect x="168" y="16" width="5" height="56" fill="var(--gold)"/>
    <text x="30" y="78">Category 1</text><text x="72" y="78">Category 2</text><text x="114" y="78">Category 3</text><text x="156" y="78">Category 4</text>
  </svg>
  <p class="abs txt" style="left:30px;top:140px;width:170px">The chart compares case numbers across four service areas over the last reporting period, grouped by quarter.</p>
  <div class="abs" style="left:232px;top:56px;width:110px"><div class="small-h" style="font-size:4.8px;font-weight:700"><span style="display:inline-block;width:6px;height:6px;background:var(--navy);margin-right:3px"></span>Heading Goes Here</div><p class="txt" style="padding-left:9px">Short note about this data series.</p></div>
  <div class="abs" style="left:232px;top:96px;width:110px"><div class="small-h" style="font-size:4.8px;font-weight:700;color:var(--green)"><span style="display:inline-block;width:6px;height:6px;background:var(--green);margin-right:3px"></span>Heading Goes Here</div><p class="txt" style="padding-left:9px">Short note about this data series.</p></div>
  <div class="abs" style="left:232px;top:136px;width:110px"><div class="small-h" style="font-size:4.8px;font-weight:700;color:var(--gold)"><span style="display:inline-block;width:6px;height:6px;background:var(--gold);margin-right:3px"></span>Heading Goes Here</div><p class="txt" style="padding-left:9px">Short note about this data series.</p></div>
  <div class="foot"><div class="brand"><span class="dot"></span><span class="name">Tierpraxamo</span></div><div class="rights">© Tierpraxamo 2023. All Rights Reserved.<span class="pg"></span></div></div>
</section>

<section class="slide c2 r8">
  <div class="abs" style="left:18px;top:16px"><div class="h"><b>TABLE</b> SLIDE</div><div class="bars"><i></i><i></i><i></i></div></div>
  <div class="abs" style="left:118px;top:46px;width:56px;height:132px;border:1.5px solid var(--navy);border-radius:4px;z-index:2"></div>
  <table class="data abs" style="left:18px;top:52px;width:326px">
    <tr><th style="background:var(--navy)">Heading Goes Here</th><th style="background:var(--navy)">Heading<br>Goes Here</th><th style="background:var(--green)">Heading<br>Goes Here</th><th style="background:var(--gold)">Heading<br>Goes Here</th><th style="background:var(--rust)">Heading<br>Goes Here</th></tr>
    <tr><td>Lorem ipsum dolor sit amet</td><td>1678</td><td>433</td><td>2000</td><td>1200</td></tr>
    <tr><td>Vivamus eu dui ex. Curabitur dapibus</td><td>1122</td><td>1244</td><td>8000</td><td>4500</td></tr>
    <tr><td>Praesent aliquet lorem ex, eu dapibus</td><td>1542</td><td>7890</td><td>1699</td><td>3222</td></tr>
    <tr><td>Duis eget tellus porta, consequat lacus</td><td>2890</td><td>1267</td><td>5600</td><td>6700</td></tr>
    <tr><td>Donec risus orci, gravida sit amet</td><td>3122</td><td>5412</td><td>1200</td><td>8935</td></tr>
    <tr><td>Nunc placerat, arcu nec mattis</td><td>5167</td><td>6711</td><td>4500</td><td>1255</td></tr>
    <tr><td>Nam semper tristique mauris</td><td>2004</td><td>3159</td><td>8100</td><td>1290</td></tr>
  </table>
  <div class="foot"><div class="brand"><span class="dot"></span><span class="name">Tierpraxamo</span></div><div class="rights">© Tierpraxamo 2023. All Rights Reserved.<span class="pg"></span></div></div>
</section>

<section class="slide c3 r8" style="background:var(--navy)">
  <div class="abs" style="left:0;top:52px;width:300px;height:100px;background:#fff"></div>
  <div class="ring" style="left:206px;top:32px;width:138px;height:138px;background:var(--gold)"></div>
  <div class="ring" style="left:218px;top:48px;width:104px;height:104px;background:#fff"></div>
  <div class="ring" style="left:224px;top:54px;width:92px;height:92px;background:var(--navy)"></div>
  <div class="brand abs on-dark" style="left:18px;top:20px"><span class="dot"></span><span class="name">Tierpraxamo</span></div>
  <div class="abs" style="left:29px;top:76px;font-size:7px;font-weight:500;color:var(--navy)">CONTACT US</div>
  <ul class="abs" style="left:29px;top:92px;list-style:none;font-size:4.6px;color:var(--navy);line-height:10px">
    <li><svg width="6" height="6" viewBox="0 0 6 6" style="vertical-align:middle;margin-right:4px"><path d="M1 0l1.5 1.6-.8 1 1.7 1.7 1-.8L6 5l-1 1C2 6 0 3.5 0 1z" fill="var(--gold)"/></svg>Phone Number Goes Here</li>
    <li><svg width="6" height="6" viewBox="0 0 6 6" style="vertical-align:middle;margin-right:4px"><rect x=".5" y="1" width="5" height="4" fill="none" stroke="var(--gold)"/><path d="M.5 1l2.5 2 2.5-2" fill="none" stroke="var(--gold)"/></svg>E-Mail Address Goes Here</li>
    <li><svg width="6" height="6" viewBox="0 0 6 6" style="vertical-align:middle;margin-right:4px"><circle cx="3" cy="3" r="2.5" fill="none" stroke="var(--gold)"/><path d="M.5 3h5M3 .5v5" stroke="var(--gold)" stroke-width=".6"/></svg>URL Address Goes Here</li>
  </ul>
  <div class="abs fine" style="left:20px;top:178px;color:#fff">© Tierpraxamo 2023. All Rights Reserved.</div>
</section>

</body>
</html>
```